Wrap on a Dravo truck with a topper the focus is Roofing.
The company name Pellick Construction, I have attached a business card.
I have attached their current bill board in town that should have all the info you need to design the wrap. I have also attached picture of the truck

```html
<!DOCTYPE html>
<html lang="en">
<head>
<meta charset="utf-8">
<title>Pellick Construction – Truck Wrap</title>
<link href="https://fonts.googleapis.com/css2?family=Oswald:wght@500;700&family=Montserrat:wght@600&display=swap" rel="stylesheet">
<style>
  :root {
    --page: #f2f2f2;
    --body-grey: #a3a4a7;
    --grey-dark: #7d7e81;
    --band-black: #141414;
    --band-mid: #2b2b2b;
    --white: #ffffff;
    --photo-sky: #b9c3c9;
    --photo-house: #8a8f93;
    --photo-lawn: #6f7d52;
  }
  html, body {
    margin: 0;
    width: 1200px;
    height: 916px;
    overflow: hidden;
    background: var(--page);
  }
  .wrap-sheet { display: block; width: 1200px; height: 916px; }
  .panel-body { fill: var(--body-grey); }
  .panel-band { fill: url(#bandShade); }
  .panel-stripe { fill: none; stroke: var(--white); stroke-width: 12; stroke-linejoin: round; }
  .web-strip { fill: var(--white); }
  .phone { font-family: "Oswald", sans-serif; font-weight: 700; font-size: 33px; fill: var(--white); letter-spacing: 0.5px; }
  .company-name { font-family: "Oswald", sans-serif; font-weight: 700; font-size: 32px; fill: var(--white); letter-spacing: 0.5px; }
  .services { font-family: "Montserrat", sans-serif; font-weight: 600; font-size: 13px; fill: var(--white); letter-spacing: 1.5px; }
  .web { font-family: "Montserrat", sans-serif; font-weight: 600; font-size: 11px; fill: var(--band-black); }
  .selling-point { font-family: "Oswald", sans-serif; font-weight: 700; font-size: 16px; fill: var(--white); }
  .brand-mark { font-family: "Oswald", sans-serif; font-weight: 700; font-size: 40px; fill: var(--white); }
  .brand-ring { fill: var(--band-black); stroke: var(--white); stroke-width: 6; }
</style>
</head>
<body>
<svg class="wrap-sheet" viewBox="0 0 1452 1108" xmlns="http://www.w3.org/2000/svg">
  <defs>
    <linearGradient id="bandShade" x1="0" y1="0" x2="1" y2="0">
      <stop offset="0" stop-color="#262626"/>
      <stop offset="0.5" stop-color="#0f0f0f"/>
      <stop offset="1" stop-color="#2a2a2a"/>
    </linearGradient>
    <linearGradient id="toppersPhoto" x1="0" y1="0" x2="0" y2="1">
      <stop offset="0" stop-color="#b9c3c9"/>
      <stop offset="0.55" stop-color="#8a8f93"/>
      <stop offset="1" stop-color="#6f7d52"/>
    </linearGradient>
    <g id="sideGraphics">
      <rect class="panel-body" x="165" y="242" width="1195" height="168" rx="14"/>
      <path class="panel-band" d="M170 245 L1122 250 L1062 410 L560 410 L522 300 L170 290 Z"/>
      <path class="panel-stripe" d="M175 292 L522 302 L558 406"/>
      <path class="panel-stripe" d="M1122 250 L1060 408"/>
      <rect class="web-strip" x="1125" y="270" width="176" height="28" rx="3"/>
    </g>
  </defs>

  <!-- Driver side -->
  <g class="side side-driver">
    <rect x="172" y="120" width="493" height="118" fill="url(#toppersPhoto)" role="img" aria-label="Photo of a finished residential roof on a white house"/>
    <use href="#sideGraphics"/>
    <text class="selling-point" x="340" y="183">• STORM</text>
    <text class="selling-point" x="340" y="201">• DAMAGE</text>
    <text class="selling-point" x="340" y="219">• EXPERTS</text>
    <text class="selling-point" x="418" y="183">• LICENSED</text>
    <text class="selling-point" x="418" y="201">• INSURED</text>
    <text class="selling-point" x="418" y="219">• &amp; LOCAL</text>
    <text class="phone" x="264" y="281">555.014.2260</text>
    <circle class="brand-ring" cx="676" cy="318" r="72"/>
    <text class="brand-mark" x="676" y="332" text-anchor="middle">Pellick</text>
    <text class="company-name" x="913" y="325" text-anchor="middle">PELLICK CONSTRUCTION</text>
    <text class="services" x="913" y="344" text-anchor="middle">ROOFING - SIDING - GUTTERS</text>
    <text class="web" x="1220" y="289" text-anchor="middle">pellickconstructiontn.com</text>
  </g>

  <!-- Passenger side -->
  <g class="side side-passenger">
    <g transform="translate(1460,555) scale(-1,1)">
      <rect x="172" y="120" width="493" height="118" fill="url(#toppersPhoto)" role="img" aria-label="Photo of a finished residential roof on a white house"/>
      <use href="#sideGraphics"/>
    </g>
    <text class="selling-point" x="963" y="738">• STORM</text>
    <text class="selling-point" x="963" y="756">• DAMAGE</text>
    <text class="selling-point" x="963" y="774">• EXPERTS</text>
    <text class="selling-point" x="1041" y="738">• LICENSED</text>
    <text class="selling-point" x="1041" y="756">• INSURED</text>
    <text class="selling-point" x="1041" y="774">• &amp; LOCAL</text>
    <text class="phone" x="1010" y="836">555.014.2260</text>
    <circle class="brand-ring" cx="778" cy="873" r="72"/>
    <text class="brand-mark" x="778" y="887" text-anchor="middle">Pellick</text>
    <text class="company-name" x="538" y="878" text-anchor="middle">PELLICK CONSTRUCTION</text>
    <text class="services" x="538" y="897" text-anchor="middle">ROOFING - SIDING - GUTTERS</text>
    <text class="web" x="247" y="844" text-anchor="middle">pellickconstructiontn.com</text>
  </g>
</svg>
</body>
</html>
```